Gavin Holloway Advisory - Web Design Project

We need a web design for my new edgy consulting business specializing in innovation, technology and strategy.

It is our personal goal to turn each client into raving fans by helping them achieve their own business goals and aspirations through assisting them in raising their own innovation and marketing standards.

We provide our personalised and state-of-the-art services to our clients and boards who represent some of the world greatest innovative thinkers.

Here is some other information which may help shape your thinking.

I've had direct Involvement in the development of the following iPad, iPhone Applications and websites

PelicanTrailsHub.com (TerraLoom platform) by Coastline Visitor Bureau
http://pelicantrailshub.example

Harbor Zest by Tidy Sailways
https://apps.example.net/au/app/harbor-zest/id900111222

RedDustGo by Frontier Visits Office
https://apps.example.net/au/app/reddustgo/id900111333

Wexbridge Rambles
http://www.wexbridgerambles.example

Trip Weaver by Coastline Visitor Bureau
http://apps.example.net/au/app/trip-weaver/id900111444

Sunward by Sunward Travel Board
https://apps.example.net/au/app/sunward/id900111555

Fernvale Ridge Road Loop by Roamwell Agency
https://apps.example.net/au/app/fernvale-ridge-road-loop/id900111666

Pathfinder Run by Frontier Visits Office and Southern Coast Visitor Council
https://apps.example.net/au/app/pathfinder-run-grand-trek/id900111777

Gavin Holloway Advisory (GHA)
November 2012 – Present (8 months)Brisbane, Sydney, Canberra

Gavin’s consults to Small-to-Medium Enterprises (SME) and Government organisations on business strategy, technology strategy, risk mitigation, disruptive technology and innovation in the workplace.

Gavin’s consultancy mantra is that we cannot divorce economic life from cultural life particularly in an era when social capital may be as important as physical capital in business.

Reason: request from designers, I want to see their best efforts

Target Market(s)

35+

Industry/Entity Type

Business

Requirements
Must have
• Please use some of the personal image(s) contained in the zip files which can be downloaded from here

http://filedrop.example/k7Pq2Lm9
http://filedrop.example/r4Tz8Hv1
http://filedrop.example/w6Nc3Bx5
Nice to have
• Black, Sleek design, maybe minimalist. Nice to have a Glint for the design. Nice to have it easily ported to Wordpress or be a modified Wordpress template. HTML 5, responsive design

```html
<!DOCTYPE html>
<html lang="en">
<head>
<meta charset="utf-8">
<title>Gavin Holloway Advisory</title>
<link rel="stylesheet" href="https://fonts.googleapis.com/css2?family=Source+Sans+3:wght@300;400;600;700&display=swap">
<style>
:root{
  --page-bg:#f8f8f8;
  --tab-active:#5b5a61;
  --ink:#1f1f22;
  --ink-soft:#7d7f82;
  --nav-ink:#222226;
  --hero-light:#eef1ef;
  --hero-mid:#d6dcd8;
  --hero-green:#b9c9ad;
  --suit:#8d9cad;
  --suit-dark:#5f6d7c;
  --circle-one:#3d3f40;
  --circle-two:#23222e;
  --circle-three:#5a5a5e;
  --white:#ffffff;
}
*{margin:0;padding:0;box-sizing:border-box}
html,body{width:1200px;height:1000px;overflow:hidden}
body{background:var(--page-bg);font-family:"Source Sans 3",Arial,sans-serif;color:var(--ink);position:relative}

.site-header{position:absolute;left:0;top:0;width:1200px;height:277px}
.main-nav{position:absolute;left:83px;top:0;display:flex}
.nav-item{width:103px;height:204px;display:flex;flex-direction:column;align-items:center;padding-top:84px;color:var(--nav-ink);font-size:19px;line-height:1.25;text-align:center;text-decoration:none}
.nav-item svg{width:36px;height:36px;margin-bottom:18px}
.nav-item.is-active{background:var(--tab-active);color:var(--white)}
.nav-item.about{margin-left:39px}
.nav-item.why{margin-left:42px}
.nav-item.contact{margin-left:42px}

.brand{position:absolute;right:88px;top:36px;text-align:center;color:#3b3b3f}
.brand-name{font-weight:300;font-size:54px;letter-spacing:4px;line-height:1}
.brand-tagline{font-weight:300;font-size:15px;line-height:1.2;margin-top:4px}

.hero{position:absolute;left:0;top:277px;width:1200px;height:450px;background:linear-gradient(90deg,#dfe4e1 0%,var(--hero-light) 30%,var(--hero-green) 55%,var(--hero-mid) 75%,#e9eee9 100%)}
.hero-portrait{position:absolute;left:662px;top:168px;width:538px;height:559px;background:linear-gradient(180deg,#d9c2b0 0%,#cfb7a5 28%,var(--suit) 45%,var(--suit-dark) 100%);border-radius:240px 240px 0 0}
.hero-copy{position:absolute;left:151px;top:365px;font-size:39px;line-height:50px;font-weight:300;color:var(--ink-soft)}
.hero-copy strong{font-weight:700;color:var(--ink)}
.hero-signature{position:absolute;left:365px;top:600px;width:296px;height:54px;background:rgba(40,40,45,.12);border-radius:4px}

.services{position:absolute;left:0;top:727px;width:1200px;height:273px;background:var(--page-bg)}
.service-badge{position:absolute;top:91px;width:202px;height:202px;border-radius:50%;display:flex;align-items:flex-start;justify-content:center;padding-top:52px}
.service-badge svg{width:84px;height:84px}
.service-badge.research{left:156px;background:var(--circle-one)}
.service-badge.technology{left:513px;background:var(--circle-two)}
.service-badge.strategy{left:851px;background:var(--circle-three)}
</style>
</head>
<body>
<header class="site-header">
  <nav class="main-nav">
    <a class="nav-item is-active" href="#">
      <svg viewBox="0 0 24 24"><path d="M12 3 2 12h3v9h5v-6h4v6h5v-9h3z" fill="currentColor"/></svg>
      Home
    </a>
    <a class="nav-item about" href="#">
      <svg viewBox="0 0 24 24" fill="none" stroke="currentColor" stroke-width="2"><circle cx="10" cy="8" r="4"/><path d="M3 21c0-4 3-7 7-7s7 3 7 7z"/><path d="M15 4a4 4 0 0 1 0 8M19 21c0-3-1-5-3-6"/></svg>
      About<br>Us
    </a>
    <a class="nav-item why" href="#">
      <svg viewBox="0 0 24 24" fill="none" stroke="currentColor" stroke-width="2.4"><circle cx="10" cy="10" r="7"/><path d="M15 15l6 6M10 6.5v7M6.5 10h7"/></svg>
      Why<br>Choose Us?
    </a>
    <a class="nav-item contact" href="#">
      <svg viewBox="0 0 24 24" fill="none" stroke="currentColor" stroke-width="2.2"><rect x="2.5" y="5" width="19" height="14" rx="1.5"/><path d="M3 6l9 7 9-7"/></svg>
      Contact<br>Us
    </a>
  </nav>
  <div class="brand">
    <div class="brand-name">GHA</div>
    <div class="brand-tagline">gavin holloway<br>advisory</div>
  </div>
</header>

<section class="hero" role="img" aria-label="Bright office interior with large white-framed windows and greenery outside"></section>
<div class="hero-portrait" role="img" aria-label="Portrait of Gavin Holloway in a grey suit and light blue shirt"></div>
<p class="hero-copy">We are new edgy<br><strong>Consulting Business</strong><br>specializing in innovation,<br>technology and strategy.</p>
<div class="hero-signature" role="img" aria-label="Handwritten signature of Gavin Holloway"></div>

<section class="services">
  <div class="service-badge research">
    <svg viewBox="0 0 24 24"><path d="M9 2h6v1.5h-1v5.5l6 11c.5 1-.2 2-1.3 2H5.3c-1.1 0-1.8-1-1.3-2l6-11V3.5H9z" fill="#fff"/></svg>
  </div>
  <div class="service-badge technology">
    <svg viewBox="0 0 24 24"><rect x="3" y="3" width="18" height="18" rx="1" fill="#fff"/><rect x="5" y="7" width="14" height="12" fill="#23222e"/><circle cx="5.5" cy="5" r=".8" fill="#23222e"/><circle cx="8" cy="5" r=".8" fill="#23222e"/><circle cx="10.5" cy="5" r=".8" fill="#23222e"/><path d="M10 10l7 3-3 1 2 3-1.3 1-2-3-2 2z" fill="#fff"/></svg>
  </div>
  <div class="service-badge strategy">
    <svg viewBox="0 0 24 24"><circle cx="12" cy="12" r="6.5" fill="#fff"/><ellipse cx="12" cy="12" rx="11" ry="3.5" transform="rotate(-25 12 12)" fill="none" stroke="#fff" stroke-width="1.6"/></svg>
  </div>
</section>
</body>
</html>
```